Business Card Design

We are looking for a double sided business card.

On one side would be our logo

On the Other Side

Martin Kolby
Sales and Marketing

Phone/Text Logo and 530-418-2763
Email Logo and info@plumvalepets.com
Website Logo and www.plumvalepets.com
Facebook Logo and plumvale pets
Instagram Logo and plumvale_pets

Target Market(s)

Pet owners

Contact Information for Business Card

In project description

Requirements
Must have
• Logo

```html
<!DOCTYPE html>
<html lang="en">
<head>
<meta charset="utf-8">
<title>Plumvale Pets – Business Card</title>
<link rel="stylesheet" href="https://fonts.googleapis.com/css2?family=Montserrat:wght@400;500;700;800&display=swap">
<style>
  :root {
    --backdrop: #3b3b3b;
    --card: #161616;
    --gold: #f5a712;
    --amber: #f28c0f;
    --silver: #e6e6e6;
    --text: #e9e9e9;
    --rule: #b7860f;
  }
  * { box-sizing: border-box; margin: 0; padding: 0; }
  html, body {
    width: 1200px; height: 791px; overflow: hidden;
    background: var(--backdrop);
    font-family: "Montserrat", Arial, sans-serif;
  }
  .sheet {
    width: 1200px; height: 791px;
    display: flex; align-items: center; justify-content: center; gap: 40px;
  }
  .card {
    width: 540px; height: 309px;
    background: var(--card);
    border-bottom: 3px solid var(--amber);
    position: relative;
    box-shadow: 0 18px 30px rgba(0,0,0,.35);
  }
  /* contact side */
  .card--contact { display: flex; align-items: center; }
  .brand-block {
    width: 250px; height: 100%;
    display: flex; flex-direction: column; align-items: center; justify-content: center; gap: 10px;
  }
  .brand-name {
    display: flex; align-items: center; gap: 10px;
    color: var(--gold); font-weight: 800; font-size: 24px; letter-spacing: 1px;
    text-transform: uppercase;
  }
  .brand-dot { width: 14px; height: 14px; border-radius: 50%; background: var(--gold); }
  .brand-url {
    color: var(--gold); font-size: 9px; font-weight: 500; letter-spacing: 2.5px; text-transform: uppercase;
  }
  .divider { width: 1px; height: 130px; background: var(--rule); }
  .contact-block { padding-left: 34px; }
  .person-name {
    color: var(--gold); font-weight: 800; font-size: 19px; text-transform: uppercase; letter-spacing: .3px;
  }
  .person-role { color: var(--text); font-size: 14px; margin-top: 2px; }
  .contact-list { list-style: none; margin-top: 26px; display: grid; gap: 7px; }
  .contact-list li {
    display: flex; align-items: center; gap: 10px;
    color: var(--text); font-size: 14px;
  }
  .contact-list svg { width: 12px; height: 12px; flex: none; }
  /* logo side */
  .card--logo { display: flex; align-items: center; justify-content: center; }
  .card--logo .brand-name { font-size: 32px; }
  .card--logo .brand-dot { width: 18px; height: 18px; }
</style>
</head>
<body>
<main class="sheet">
  <section class="card card--contact" aria-label="Contact side">
    <div class="brand-block">
      <div class="brand-name"><span class="brand-dot"></span>Plumvale Pets</div>
      <div class="brand-url">www.plumvalepets.com</div>
    </div>
    <div class="divider"></div>
    <div class="contact-block">
      <h1 class="person-name">Martin Kolby</h1>
      <p class="person-role">Sales and Marketing</p>
      <ul class="contact-list">
        <li>
          <svg viewBox="0 0 12 12" aria-hidden="true"><path fill="#f5a712" d="M2.4 1 4.2 2.8 3.3 4.1c.6 1.3 1.5 2.2 2.6 2.7l1.3-.9L9 7.7 7.9 9.5C4.7 9.3 2.6 7.2 1.3 3.9z"/></svg>
          530-418-2763
        </li>
        <li>
          <svg viewBox="0 0 12 12" aria-hidden="true"><rect x="1" y="2.5" width="10" height="7" rx="1" fill="#f5a712"/><path d="M1.5 3 6 6.5 10.5 3" stroke="#161616" fill="none"/></svg>
          info@plumvalepets.com
        </li>
        <li>
          <svg viewBox="0 0 12 12" aria-hidden="true"><circle cx="6" cy="6" r="5" fill="#f5a712"/><path d="M1 6h10M6 1c-2 2.5-2 7.5 0 10M6 1c2 2.5 2 7.5 0 10" stroke="#161616" stroke-width=".8" fill="none"/></svg>
          www.plumvalepets.com
        </li>
        <li>
          <svg viewBox="0 0 12 12" aria-hidden="true"><rect x="1" y="1" width="10" height="10" rx="2" fill="#f5a712"/></svg>
          plumvale pets
        </li>
        <li>
          <svg viewBox="0 0 12 12" aria-hidden="true"><rect x="1.5" y="1.5" width="9" height="9" rx="2" fill="none" stroke="#f5a712" stroke-width="1.2"/></svg>
          plumvale_pets
        </li>
      </ul>
    </div>
  </section>

  <section class="card card--logo" aria-label="Logo side">
    <div class="brand-name"><span class="brand-dot"></span>Plumvale Pets</div>
  </section>
</main>
</body>
</html>
```